SkyvoraQ Business Cards and Stationary Design

Need a design for our business cards and stationary. I want to carry on the theme of the logo. I want the business cards to have a design on the back. I would like the business cards and the stationary to carry the same theme, design scheme, and branding

Target Market(s)

Airlines and Maintenance Facilities

Industry/Entity Type

Aviation

Contact Information for Business Card

Name
Position Title
Address: 4827 Tollbeck Lane, Fort Pierce, Florida, 34951
Office Number
Mobile Number
Email
Website

Font styles to use
Serif
Sans Serif

Colors

Designer to choose colors to be used in the design.

```html
<!DOCTYPE html>
<html lang="en">
<head>
<meta charset="utf-8">
<title>SkyvoraQ Business Card</title>
<link href="https://fonts.googleapis.com/css2?family=Open+Sans:wght@300;400;600;700&display=swap" rel="stylesheet">
<style>
  :root {
    --navy: #0c2a52;
    --navy-deep: #0a2347;
    --sky: #1a9be0;
    --sky-light: #3bb4f0;
    --white: #ffffff;
    --paper: #f7f8fa;
    --stage: #e7e9ed;
    --muted: #c9d6e6;
  }
  * { margin: 0; padding: 0; box-sizing: border-box; }
  html, body { width: 1200px; height: 872px; overflow: hidden; }
  body {
    background: var(--stage);
    font-family: "Open Sans", Arial, sans-serif;
    position: relative;
  }
  .card {
    position: absolute;
    width: 540px;
    height: 309px;
    border-radius: 4px;
    overflow: hidden;
    box-shadow: 0 10px 28px rgba(10, 35, 71, 0.22);
  }
  .card--back { left: 40px; top: 282px; background: var(--navy); }
  .card--front { left: 620px; top: 282px; background: var(--white); }

  /* Back */
  .back-brand {
    position: absolute; left: 0; right: 0; top: 112px;
    display: flex; align-items: center; justify-content: center; gap: 16px;
  }
  .back-brand__dot {
    width: 46px; height: 46px; border-radius: 50%;
    border: 5px solid var(--white);
  }
  .back-brand__name {
    color: var(--white); font-weight: 700; font-size: 40px; letter-spacing: 6px;
  }
  .back-url {
    position: absolute; left: 0; right: 0; top: 186px; text-align: center;
    color: var(--muted); font-size: 13px; letter-spacing: 3px;
  }

  /* Front */
  .front-shapes { position: absolute; inset: 0; }
  .front-brand {
    position: absolute; left: 34px; top: 26px;
    display: flex; flex-direction: column; align-items: center; gap: 10px;
  }
  .front-brand__dot {
    width: 58px; height: 58px; border-radius: 50%;
    border: 6px solid var(--sky);
  }
  .front-brand__name {
    color: var(--navy); font-weight: 700; font-size: 32px; letter-spacing: 6px;
  }
  .person {
    position: absolute; right: 18px; top: 124px; text-align: right; color: var(--white);
  }
  .person__name { font-weight: 700; font-size: 17px; letter-spacing: 0.5px; line-height: 1.15; }
  .person__title { font-weight: 300; font-size: 14px; letter-spacing: 0.5px; }
  .contacts {
    position: absolute; left: 34px; top: 214px; color: var(--white);
    font-size: 12px; list-style: none;
  }
  .contacts li { display: flex; align-items: center; gap: 7px; height: 19px; }
  .contacts svg { width: 12px; height: 12px; flex: none; }
  .divider {
    position: absolute; left: 222px; top: 226px; width: 1px; height: 50px;
    background: rgba(255, 255, 255, 0.35);
  }
  .address {
    position: absolute; left: 240px; top: 221px; color: var(--white);
    font-size: 12px; line-height: 19px; display: flex; gap: 7px;
  }
  .address svg { width: 12px; height: 12px; margin-top: 3px; flex: none; }
</style>
</head>
<body>

<section class="card card--back" aria-label="Business card back">
  <div class="back-brand">
    <span class="back-brand__dot"></span>
    <span class="back-brand__name">SKYVORAQ</span>
  </div>
  <p class="back-url">www.skyvoraq.com</p>
</section>

<section class="card card--front" aria-label="Business card front">
  <svg class="front-shapes" width="540" height="309" viewBox="0 0 540 309">
    <defs>
      <linearGradient id="tab-gradient" x1="0" x2="1" y1="0" y2="0">
        <stop offset="0" stop-color="#1a9be0"/>
        <stop offset="1" stop-color="#0c4f95"/>
      </linearGradient>
    </defs>
    <polygon points="0,204 540,166 540,309 0,309" fill="#0c2a52"/>
    <line x1="0" y1="203" x2="540" y2="165" stroke="#1a9be0" stroke-width="3"/>
    <path d="M330,126 L540,112 L540,168 L342,182 Q330,183 329,171 L326,138 Q325,127 330,126 Z" fill="url(#tab-gradient)"/>
    <rect x="0" y="298" width="540" height="5" fill="#1a9be0"/>
  </svg>

  <div class="front-brand">
    <span class="front-brand__dot"></span>
    <span class="front-brand__name">SKYVORAQ</span>
  </div>

  <div class="person">
    <p class="person__name">DANIEL VARROW</p>
    <p class="person__title">PRESIDENT</p>
  </div>

  <ul class="contacts">
    <li>
      <svg viewBox="0 0 12 12" fill="none" stroke="#fff" stroke-width="1"><circle cx="6" cy="6" r="5.4"/><path d="M4 3.2l1 1.6-.6.7c.4.9 1.1 1.6 2 2l.7-.6 1.6 1-.5 1c-2.2-.2-4.3-2.3-4.6-4.6z" fill="#fff" stroke="none"/></svg>
      772-555-0148
    </li>
    <li>
      <svg viewBox="0 0 12 12" fill="none" stroke="#fff" stroke-width="1"><circle cx="6" cy="6" r="5.4"/><rect x="4.2" y="2.8" width="3.6" height="6.4" rx="0.6"/></svg>
      772-555-0193
    </li>
    <li>
      <svg viewBox="0 0 12 12" fill="none" stroke="#fff" stroke-width="1"><circle cx="6" cy="6" r="5.4"/><rect x="3" y="4" width="6" height="4"/><path d="M3 4l3 2.2L9 4"/></svg>
      info@skyvoraq.com
    </li>
    <li>
      <svg viewBox="0 0 12 12" fill="none" stroke="#fff" stroke-width="1"><circle cx="6" cy="6" r="5.4"/><ellipse cx="6" cy="6" rx="2.3" ry="5.4"/><path d="M0.8 6h10.4M1.8 3.4h8.4M1.8 8.6h8.4"/></svg>
      www.skyvoraq.com
    </li>
  </ul>

  <span class="divider"></span>

  <div class="address">
    <svg viewBox="0 0 12 12" fill="none" stroke="#fff" stroke-width="1"><circle cx="6" cy="6" r="5.4"/><path d="M6 9.2C4.6 7.6 3.9 6.4 3.9 5.2a2.1 2.1 0 014.2 0c0 1.2-.7 2.4-2.1 4z"/><circle cx="6" cy="5.2" r="0.7" fill="#fff"/></svg>
    <p>4827 Tollbeck Lane, Fort Pierce,<br>Florida, 34951</p>
  </div>
</section>

</body>
</html>
```